Coin Keepers II

We need a retractable Banner designed and a 6 ft Table cling designed to complement the banner. TORVIN Financial is a registered investment advisor that offers professional investment management services. TORVIN Financial manages risk predominantly through the use of index ETF’s and protective options. Our investment style is focused on delivering superior risk weighted returns through the use of hedging and diversification. We use a long term investment horizon and follow the strictest of ethical codes to act only in the best interest of our clients. The Co- founders are Authors of a #1 best selling investment book on Quillmart called Plant and Prune. We would like to see designs that use green. Our goal at TORVIN is to provide “steady hands” to our clients financial needs.
Updates

Here are some websites for Ideas.  

Here are the options for retractable banners:

 

http://www.brixelstands.example/ProductPage.asp?cat=Retractors

 

 

Here are the ultra fit table cloths.

http://www.brixelstands.example/ProductPage.asp?id=&stype=sub&cat=Table%20Covers&sub=SnugLine+Table+Throw

 

This event will be held in a hotel.  We will have a 6ft table holding  a Computers monitor, Books, Marketing material buisness cards and giveaways.  The Sales team will be in front of the table creating potential clients.

The Template is file #4..  Thanks

Target Market(s)

Our Target market is Wealthy individuals and institutional financial advisors

Industry/Entity Type

Investment

Requirements
Must have
• Logo Hands in Green / TORVIN Financial all CAPS Black Same font
Website www.torvinfinancial.example
The banners measurements are
Product Size: Banner
(Assembled) 32.75"w x 6.875"d x 81.5"h
I have a template I can email if necessary.

Graphic Size:
(w/Bleed) 31.5"w x 85.25"h)

Viewable Area:
(Finished size) 31.5"w x 78.75"h
Nice to have
• Simplicity
Reference to Plant and Prune Book
Trust, deliberate, reliable
Seen as Experts
"Steady set of Hands
Should not have
• pictures of money, dollars signs

```html
<!DOCTYPE html>
<html lang="en">
<head>
<meta charset="utf-8">
<title>TORVIN Financial – Retractable Banner</title>
<link rel="stylesheet" href="https://fonts.googleapis.com/css2?family=EB+Garamond:ital,wght@0,700;1,400;1,700&display=swap">
<style>
  :root {
    --page: #ffffff;
    --ink: #111111;
    --ink-soft: #1e1e1e;
    --brand-green: #4a8a14;
    --panel-light: #f4f4f2;
    --panel-mid: #d6d6d4;
    --panel-dark: #7f7f7f;
    --panel-deep: #1c1c1c;
  }
  * { margin: 0; padding: 0; box-sizing: border-box; }
  html, body { width: 1200px; height: 2265px; overflow: hidden; background: var(--page); }
  .canvas { position: relative; width: 1200px; height: 2265px; font-family: "EB Garamond", Georgia, serif; }

  .banner { position: absolute; left: 194px; width: 830px; }
  .panel-top { top: 0; height: 792px;
    background: linear-gradient(115deg, var(--panel-light) 0%, #e2e2e0 45%, #b4b4b2 75%, var(--panel-dark) 100%); }
  .panel-middle { top: 910px; height: 832px;
    background: linear-gradient(160deg, #f0f0ee 0%, #c8c8c6 40%, #9d9d9b 75%, #6e6e6e 100%); }
  .panel-bottom { top: 1856px; height: 400px;
    background: linear-gradient(155deg, #bdbdbb 0%, #8a8a8a 45%, #505050 75%, var(--panel-deep) 100%); }

  .tile-band { position: absolute; left: 194px; width: 830px; height: 102px; display: flex; gap: 12px; }
  .tile-band--upper { top: 804px; }
  .tile-band--lower { top: 1748px; }
  .tile { height: 100%; flex: 0 0 104px; }
  .tile:first-child { flex-basis: 48px; }
  .tile:last-child { flex-basis: 74px; }

  .logo-mark { position: absolute; left: 519px; top: 250px; width: 180px; height: 180px; background: var(--brand-green); }
  .brand-name { position: absolute; left: 194px; width: 830px; top: 640px; text-align: center;
    font-weight: 700; font-size: 78px; letter-spacing: 3px; color: var(--ink); line-height: 1; }

  .tip { position: absolute; font-style: italic; font-weight: 700; font-size: 42px; line-height: 1.5;
    color: var(--ink-soft); text-shadow: 2px 3px 3px rgba(0,0,0,0.35); white-space: nowrap; }
  .trail { position: absolute; width: 230px; height: 12px; }
  .trail--long { width: 400px; }

  .web-address { position: absolute; left: 194px; width: 830px; top: 1906px; text-align: center;
    font-weight: 700; font-size: 62px; color: var(--ink); line-height: 1; letter-spacing: 1px; }
  .web-address .tld { font-style: italic; font-weight: 400; font-size: 38px; letter-spacing: 0; }
  .footer-mark { position: absolute; left: 564px; top: 2012px; width: 90px; height: 90px; background: var(--brand-green); }
</style>
</head>
<body>
<div class="canvas">
  <section class="banner panel-top"></section>
  <div class="logo-mark"></div>
  <h1 class="brand-name">TORVIN FINANCIAL</h1>

  <div class="tile-band tile-band--upper">
    <span class="tile" style="background:#9dc383"></span>
    <span class="tile" style="background:#8cbd70"></span>
    <span class="tile" style="background:#6fa447"></span>
    <span class="tile" style="background:#4d8c1f"></span>
    <span class="tile" style="background:#4a7f25"></span>
    <span class="tile" style="background:#46603a"></span>
    <span class="tile" style="background:#384430"></span>
    <span class="tile" style="background:#2a2e28"></span>
  </div>

  <section class="banner panel-middle"></section>

  <p class="tip" style="left:280px; top:962px;">Hedge Every Investment</p>
  <svg class="trail" style="left:780px; top:980px;" viewBox="0 0 230 12" aria-hidden="true">
    <g fill="#4a8a14"><rect x="0" y="1" width="30" height="10"/><rect x="38" y="1" width="18" height="10"/><rect x="64" y="2" width="14" height="8"/><rect x="94" y="2" width="10" height="8"/><rect x="128" y="3" width="8" height="6" opacity=".8"/><rect x="166" y="3" width="6" height="6" opacity=".6"/><rect x="206" y="3" width="6" height="6" opacity=".45"/></g>
  </svg>

  <svg class="trail" style="left:200px; top:1104px;" viewBox="0 0 230 12" aria-hidden="true">
    <g fill="#4a8a14"><rect x="0" y="3" width="6" height="6" opacity=".45"/><rect x="40" y="3" width="6" height="6" opacity=".6"/><rect x="78" y="3" width="8" height="6" opacity=".8"/><rect x="110" y="2" width="10" height="8"/><rect x="136" y="2" width="14" height="8"/><rect x="158" y="1" width="18" height="10"/><rect x="184" y="1" width="46" height="10"/></g>
  </svg>
  <p class="tip" style="left:464px; top:1084px;">Know Your Risk Metrics</p>

  <p class="tip" style="left:276px; top:1210px;">A Smart Portfolio=</p>
  <svg class="trail" style="left:704px; top:1224px;" viewBox="0 0 230 12" aria-hidden="true">
    <g fill="#4a8a14"><rect x="0" y="1" width="30" height="10"/><rect x="38" y="1" width="18" height="10"/><rect x="64" y="2" width="14" height="8"/><rect x="94" y="2" width="10" height="8"/><rect x="128" y="3" width="8" height="6" opacity=".8"/><rect x="166" y="3" width="6" height="6" opacity=".6"/><rect x="206" y="3" width="6" height="6" opacity=".45"/></g>
  </svg>
  <p class="tip" style="left:276px; top:1274px;">Long Term+ Diversification</p>

  <svg class="trail" style="left:196px; top:1428px;" viewBox="0 0 230 12" aria-hidden="true">
    <g fill="#4a8a14"><rect x="0" y="3" width="6" height="6" opacity=".45"/><rect x="40" y="3" width="6" height="6" opacity=".6"/><rect x="78" y="3" width="8" height="6" opacity=".8"/><rect x="110" y="2" width="10" height="8"/><rect x="136" y="2" width="14" height="8"/><rect x="158" y="1" width="18" height="10"/><rect x="184" y="1" width="46" height="10"/></g>
  </svg>
  <p class="tip" style="left:426px; top:1408px;">Unleash Your Inner Guru</p>

  <p class="tip" style="left:276px; top:1536px;">Harvest Your Gains and Losses</p>
  <svg class="trail trail--long" style="left:580px; top:1604px;" viewBox="0 0 400 12" aria-hidden="true">
    <g fill="#4a8a14"><rect x="0" y="1" width="40" height="10"/><rect x="50" y="1" width="24" height="10"/><rect x="84" y="2" width="16" height="8"/><rect x="124" y="2" width="12" height="8"/><rect x="176" y="3" width="8" height="6" opacity=".8"/><rect x="240" y="3" width="6" height="6" opacity=".6"/><rect x="310" y="3" width="6" height="6" opacity=".45"/><rect x="380" y="3" width="6" height="6" opacity=".35"/></g>
  </svg>

  <div class="tile-band tile-band--lower">
    <span class="tile" style="background:#3d4a32"></span>
    <span class="tile" style="background:#4a6a30"></span>
    <span class="tile" style="background:#4a871c"></span>
    <span class="tile" style="background:#5a9a2d"></span>
    <span class="tile" style="background:#72a94e"></span>
    <span class="tile" style="background:#9bc681"></span>
    <span class="tile" style="background:#b7d8a3"></span>
    <span class="tile" style="background:#d6e9c9"></span>
  </div>

  <section class="banner panel-bottom"></section>
  <p class="web-address">TORVINFINANCIAL<span class="tld">.example</span></p>
  <div class="footer-mark"></div>
</div>
</body>
</html>
```